Brochure for a civil enineering company in A4 format

I need a brochure design for our company VELTA Engineering S.r.l.. We are an engineering consultant company. Our main clients are from the infrastructure industry (geotechnical and underground sectors mainly).
We are looking for a 2 pages (4 faces) fold out design with a glued pocket where we can put individual data sheets.
I need A4 format pages.

Target Market(s)

We are an engineering consultant company. Our main clients are from the infrastructure industry (geotechnical and underground sectors mainly).

Industry/Entity Type

Civil Engineer

Font styles to use
Sans Serif

Requirements
Must have
• Overall: 2 pages in A4 format
Essential style. Bright and modern appearance.
Glued pocket
Logo integrated in a picture on the pocket where I would like to insert a slogan (… velta engineering … reliable solutions …)
Attached are selected images which the designer can use and edit at their own discretion.
Some advice in the following (anyway designers are free to provide their solutions):
Outer sheets:
Front page with name, logo. It could be nice to have the “m” of the logo integrated in a pictures, also a modified picture (I mean modify one of the attached pictures) so to create a general image and do not tie the cover to a specific job.
Back page: offices address and contact email address. Nice to have one space for a slogan.
Inner sheet: text that I upload in the file “inside-sheets”, possibly with pictures on each sheet. In the right faces insert the glued pocket. On this pages insert the section OUR EXPERIENCE ….with a space for a picture of our team.
Nice to have
• Clean and essential design.
Pictures choosing from the atteched ones. Pictures could be modified in a very light manner to make them a general idea of the work ( I mean geotechnical world) without to be immediately linked to a specific site.
Should not have
• excessive frills

```html
<!DOCTYPE html>
<html lang="it">
<head>
<meta charset="utf-8">
<title>VELTA Engineering – Brochure</title>
<link href="https://fonts.googleapis.com/css2?family=Montserrat:wght@400;500;600;700;800&display=swap" rel="stylesheet">
<style>
  :root{
    --canvas:#ececed;
    --paper:#ffffff;
    --paper-grey:#dcdcdd;
    --band:#d4d4d5;
    --ink:#111111;
    --ink-soft:#3a3a3a;
    --on-dark:#f2f2f2;
  }
  *{box-sizing:border-box;margin:0;padding:0}
  html,body{width:1200px;height:2403px;overflow:hidden}
  body{background:var(--canvas);font-family:"Montserrat",Arial,sans-serif;color:var(--ink);position:relative}

  .spread{position:absolute;left:40px;width:1120px;height:792px;display:flex;box-shadow:0 8px 28px rgba(0,0,0,.18)}
  .spread--outer{top:300px}
  .spread--inner{top:1320px}
  .page{position:relative;width:560px;height:792px;overflow:hidden;background:var(--paper)}
  .page--grey{background:var(--paper-grey)}
  .layer{position:absolute;left:0;top:0}

  /* back cover */
  .contacts{position:absolute;left:0;width:560px;top:372px;text-align:center}
  .brand-small{font-weight:800;font-size:30px;letter-spacing:1px;line-height:1}
  .slogan-small{font-size:5.5px;letter-spacing:1.6px;text-transform:uppercase;margin-top:5px;font-weight:600}
  .offices-title{font-weight:700;font-size:13px;line-height:1.2;margin-top:34px;text-transform:uppercase}
  .city{font-weight:700;font-size:11px;margin-top:20px;text-transform:uppercase}
  .address{font-size:9px;line-height:1.45;margin-top:6px;color:var(--ink-soft)}
  .city--second{margin-top:44px}

  /* front cover */
  .cover-band{position:absolute;left:0;top:560px;width:560px;height:140px;background:var(--band)}
  .brand-large{position:absolute;left:0;width:560px;top:584px;text-align:center;font-weight:800;font-size:92px;letter-spacing:2px;line-height:1}

  /* inner pages */
  .section-title{font-weight:800;font-size:13px;text-transform:uppercase;letter-spacing:.3px}
  .copy{font-size:7.6px;line-height:1.45;text-align:justify;margin-top:7px}
  .company{position:absolute;left:46px;top:22px;width:450px;color:var(--on-dark)}
  .company .section-title{color:#fff}
  .services{position:absolute;left:46px;top:480px;width:470px}
  .bullets{list-style:none;margin-top:12px}
  .bullets li{position:relative;padding-left:14px;font-size:7.6px;line-height:1.45;margin-top:10px}
  .bullets li::before{content:"";position:absolute;left:2px;top:3px;width:5px;height:5px;border-radius:50%;background:var(--ink)}
  .expertise{position:absolute;left:30px;top:262px;width:490px}
</style>
</head>
<body>

<section class="spread spread--outer">
  <div class="page page--back">
    <div class="contacts">
      <p class="brand-small">VELTA</p>
      <p class="slogan-small">velta engineering · reliable solutions</p>
      <p class="offices-title">Our<br>Offices</p>
      <p class="city">Milano</p>
      <p class="address">Via dei Tigli, 14<br>20100 Milano - IT<br>T: +39 02 5550 1840<br>E: info@veltaeng.example</p>
      <p class="city city--second">Arco TN</p>
      <p class="address">Via delle Querce, 9<br>38062 Arco TN - IT<br>T: +39 02 5550 1840<br>E: info@veltaeng.example</p>
    </div>
  </div>

  <div class="page page--front">
    <svg class="layer" style="top:210px;left:0" width="560" height="350" viewBox="0 0 560 350" role="img" aria-label="Photo of an underground construction site seen from above, with machinery and steel reinforcement">
      <defs>
        <linearGradient id="sitePhoto" x1="0" y1="0" x2="1" y2="1">
          <stop offset="0" stop-color="#8a8178"/>
          <stop offset=".5" stop-color="#5e5750"/>
          <stop offset="1" stop-color="#3c3733"/>
        </linearGradient>
      </defs>
      <path d="M0 60 Q0 0 60 0 L500 0 Q560 0 560 60 L560 350 L0 350 Z" fill="url(#sitePhoto)"/>
    </svg>
    <div class="cover-band"></div>
    <p class="brand-large">VELTA</p>
  </div>
</section>

<section class="spread spread--inner">
  <div class="page page--company">
    <svg class="layer" width="560" height="520" viewBox="0 0 560 520" role="img" aria-label="Dark photo of a tunnel excavation face">
      <defs>
        <linearGradient id="tunnelPhoto" x1="0" y1="0" x2="0" y2="1">
          <stop offset="0" stop-color="#3d3d3f"/>
          <stop offset=".6" stop-color="#555456"/>
          <stop offset="1" stop-color="#6b6a68"/>
        </linearGradient>
      </defs>
      <path d="M0 0 L560 0 L560 340 C420 380 200 390 0 470 Z" fill="url(#tunnelPhoto)"/>
    </svg>
    <svg class="layer" style="left:395px;top:330px" width="130" height="130" viewBox="0 0 130 130" role="img" aria-label="Round inset photo of a tunnel boring machine cutter head">
      <defs>
        <radialGradient id="tbmPhoto" cx=".5" cy=".5" r=".6">
          <stop offset="0" stop-color="#a9a8a6"/>
          <stop offset="1" stop-color="#4e5256"/>
        </radialGradient>
      </defs>
      <circle cx="65" cy="65" r="62" fill="url(#tbmPhoto)" stroke="#fff" stroke-width="4"/>
    </svg>

    <div class="company">
      <h2 class="section-title">Our Company</h2>
      <p class="copy">VELTA Engineering S.r.l. offre servizi di consulenza tecnica, contrattuale e strategica di elevato livello nei settori delle scienze geologiche, dell'ingegneria geotecnica e dell'ingegneria strutturale, lavorando per mitigare il rischio e ridurre l'incertezza, con l'obiettivo di individuare la soluzione ottimale per ogni progetto.</p>
      <p class="copy">VELTA Engineering S.r.l. è una società indipendente che nasce nel luglio 2020 dall'associazione di un gruppo di professionisti che hanno maturato una lunga esperienza nel settore delle grandi opere di ingegneria civile, lavorando come direttori tecnici di importanti società di costruzione e come liberi professionisti.</p>
      <p class="copy">VELTA Engineering S.r.l. works with the experience of its founders and the enthusiasm of its people, facing every new project as a new challenge. Each of our projects represents a long term commitment: we believe in providing safe, reliable, sustainable and innovative solutions. This is and will be our distinctive character.</p>
    </div>

    <div class="services">
      <h2 class="section-title">Our Services</h2>
      <p class="copy">Progettazione e consulenza specialistica nel campo della geologia, dell'ingegneria geotecnica, delle opere sotterranee e dell'ingegneria idraulica.</p>
      <p class="copy">Aiutiamo i nostri clienti a risolvere problemi di natura progettuale, contrattuale e costruttiva che possono nascere nell'intera vita del progetto portando la nostra esperienza all'interno delle loro organizzazioni, migliorando la qualità dei loro servizi di ingegneria, ottimizzando i loro progetti, proponendo nuove idee e soluzioni, rafforzando i loro approcci.</p>
      <p class="copy">VELTA Engineering è in grado di fornire la propria assistenza nell'intero iter procedurale, dalla fase di indagine preliminare e di analisi di fattibilità fino alla progettazione costruttiva e all'assistenza tecnica in fase realizzativa.</p>
      <p class="copy">La specializzazione e l'esperienza accumulate nelle discipline della geologia, dell'ingegneria geotecnica e del sottosuolo e dell'idraulica ci permette di massimizzare la nostra efficacia quando sia necessario:</p>
      <ul class="bullets">
        <li>Far fronte a situazioni di emergenza anche su progetti in fase di sviluppo avanzato garantendo l'immediata focalizzazione delle problematiche di progetto e garantendo il risultato finale atteso (in termini di qualità, tempistiche e costi...)</li>
        <li>Fornire "second opinion" di elevato valore tecnico ed amministrativo in occasione di problematiche progettuali e costruttive e dispute legali</li>
        <li>Analizzare in tempi brevi progetti svolti da terzi individuandone le "criticità", verificandone la cantierabilità e la validità tecnico economica</li>
        <li>Ottimizzare i progetti redatti da terzi implementandone il contenuto e massimizzando l'efficacia economica degli investimenti</li>
      </ul>
    </div>
  </div>

  <div class="page page--grey page--expertise">
    <svg class="layer" width="560" height="250" viewBox="0 0 560 250" role="img" aria-label="Team photo of the four founders on a white background">
      <defs>
        <linearGradient id="teamPhoto" x1="0" y1="0" x2="1" y2="0">
          <stop offset="0" stop-color="#f4f4f4"/>
          <stop offset=".5" stop-color="#cfc7bf"/>
          <stop offset="1" stop-color="#f1f1f1"/>
        </linearGradient>
      </defs>
      <path d="M0 0 L560 0 L560 160 C470 170 360 185 290 205 C200 232 90 236 0 240 Z" fill="url(#teamPhoto)"/>
    </svg>

    <div class="expertise">
      <h2 class="section-title">Our Expertise and Experience</h2>
      <p class="copy">La società nasce dall'associazione di un gruppo di professionisti, con indiscusse competenze ed affidabilità, con esperienza maturata in oltre trent'anni di attività come progettisti e consulenti nel settore delle grandi opere di ingegneria civile, geologia, ingegneria geotecnica ed idraulica ed opere sotterranee sono il "core" delle loro competenze ...</p>
      <p class="copy">I soci fondatori sono:</p>
      <p class="copy">Marco, Già Direttore Tecnico e Socio di GALTRA Srl, nel periodo di sua permanenza fino al dicembre 2018, ha per essa firmato tutti i progetti nel campo delle opere sotterranee e la maggior parte di quelli di ingegneria geotecnica. Da gennaio 2019 è Direttore Tecnico di ITAG. Può vantare più di 150 gallerie naturali, e numerosi progetti ed assistenze tecniche nel campo delle strutture geotecniche, delle sistemazioni idrogeologiche e dei versanti e delle opere di protezione ambientale. Negli ultimi dieci anni è stato responsabile di attività di assistenza tecnica, per imprese di costruzione, di opere il cui valore supera i 440 Mio EUR e dei servizi di progettazione definitiva e/o esecutiva per opere il cui valore supera i 1.400 Mio EUR. Ha svolto attività di verifica e validazione, in Italia ed all'estero, di numerosi progetti il cui valore complessivo supera i 3.400 Mio EUR.</p>
      <p class="copy">Paolo 30 anni di esperienza professionale. Coinvolto in più di 150 gallerie naturali con lunghezza complessiva superiore a 360 km. Numerosi progetti ed attività di assistenza tecnica nel campo delle strutture, delle sistemazioni idrogeologiche e dei versanti e delle opere di protezione ambientale. Negli ultimi dieci anni responsabile di attività di assistenza tecnica in corso d'opera, per imprese di costruzione, di opere il cui valore supera i 440 Mio EUR e di servizi di progettazione definitiva o esecutiva per opere il cui valore supera i 1.400 Mio EUR. Ha svolto attività di verifica a fini della validazione, in Italia ed all'estero, di numerosi progetti il cui valore complessivo supera i 3.400 Mio EUR.</p>
      <p class="copy">Giulia 30 anni di esperienza professionale. Coinvolta in più di 150 gallerie naturali con lunghezza complessiva superiore a 360 km. Numerosi progetti ed attività di assistenza tecnica nel campo delle strutture, delle sistemazioni idrogeologiche e dei versanti e delle opere di protezione ambientale. Negli ultimi dieci anni responsabile di attività di assistenza tecnica in corso d'opera, per imprese di costruzione, di opere il cui valore supera i 440 Mio EUR e di servizi di progettazione definitiva o esecutiva per opere il cui valore supera i 1.400 Mio EUR. Ha svolto attività di verifica a fini della validazione, in Italia ed all'estero, di numerosi progetti il cui valore complessivo supera i 3.400 Mio EUR.</p>
      <p class="copy">Elena 30 anni di esperienza professionale. Coinvolta in più di 150 gallerie naturali con lunghezza complessiva superiore a 360 km. Numerosi progetti ed attività di assistenza tecnica nel campo delle strutture, delle sistemazioni idrogeologiche e dei versanti e delle opere di protezione ambientale. Negli ultimi dieci anni responsabile di attività di assistenza tecnica in corso d'opera, per imprese di costruzione, di opere il cui valore supera i 440 Mio EUR e di servizi di progettazione definitiva o esecutiva per opere il cui valore supera i 1.400 Mio EUR. Ha svolto attività di verifica a fini della validazione, in Italia ed all'estero, di numerosi progetti il cui valore complessivo supera i 3.400 Mio EUR.</p>
    </div>

    <svg class="layer" style="top:672px" width="560" height="120" viewBox="0 0 560 120" role="img" aria-label="Photo of twin tunnel portals on an earthworks site in hilly terrain">
      <defs>
        <linearGradient id="portalPhoto" x1="0" y1="0" x2="0" y2="1">
          <stop offset="0" stop-color="#6e6a5e"/>
          <stop offset=".5" stop-color="#9a927f"/>
          <stop offset="1" stop-color="#b7ad98"/>
        </linearGradient>
      </defs>
      <path d="M0 120 L0 70 C40 20 110 8 200 18 C300 28 420 20 560 4 L560 120 Z" fill="url(#portalPhoto)"/>
    </svg>
  </div>
</section>

</body>
</html>
```